Products & Services Postcard For our Vacuum Repair Store & Carpet Cleaning Company

SEE ATTACHED DOCUMENTS FOR FRONT AND BACK OF CARD.
Also, Brand logos are available in my attachments

We are a Retail Vacuum Repair shop and we also have Three carpet cleaning trucks that operate out of our location. In addition to servicing Vacuum Cleaners we also offer in home cleaning services that include: Carpet cleaning, upholstery cleaning, tile & Grout Cleaning, general cleaning services, move out clean ups, one time cleanings, post construction cleanup and strip & wax floorsWe Need to design a KTRW(nbfl kestrel lane route) postcard that shows and tells everything we do. Postcard should include all our services, have before and after pictures, list benefits of doing business with us and should have coupons attached to create urgency to call usWe:Fully Insured, commercial & Residential, free estimatesWe are the only Vacuum Store in area that is a Certified OTWAB Cleaner.Also, the only OTWAB Certified cleaner that services Vacuum Cleaners.We have a great reputation as a 5 Star Vacuum Service Station and Also a 5 Star Cleaning Company. We are a one stop shop for ALL your cleaning needs.Our goal is to educate customers and provide options.Goal of the card is to get customers to call or stop in for advice on both their vacuum cleaner and cleaning their homes. Goal is to get phone to ring or get people through the door.

Target Market(s)

Homeowners, People interested in clean

Colors

Designer to choose colors to be used in the design.

Requirements
Must have
• Before & After pics
• Coupons
• List of services
• Call to Action
• Address
• Phone #
Nice to have
• One side of postcard could be about our Vacuum Cleaner repair shop.
• The other side could be about our cleaning business

```html
<!DOCTYPE html>
<html lang="en">
<head>
<meta charset="utf-8">
<title>Harbor Vacuums – Postcard</title>
<link href="https://fonts.googleapis.com/css2?family=Roboto:wght@400;500;700&family=Oswald:wght@400;500&family=Open+Sans:wght@400;600&family=Courgette&display=swap" rel="stylesheet">
<style>
:root{
  --teal-dark:#1f4b46;
  --teal:#3f6f67;
  --sage:#7fa394;
  --sage-light:#c8d8b4;
  --grey-panel:#e3e4e3;
  --text-grey:#4d4f4f;
  --page:#d9d9d6;
  --white:#ffffff;
  --star:#f2b01e;
}
*{box-sizing:border-box;margin:0;padding:0}
html,body{width:1102px;height:1200px;overflow:hidden;background:var(--page)}
body{position:relative;font-family:"Roboto",Arial,sans-serif;color:var(--text-grey)}
.card{position:absolute;left:112px;width:878px;height:476px;background:var(--white);overflow:hidden;box-shadow:0 4px 12px rgba(0,0,0,.25)}
.card--front{top:88px}
.card--back{top:622px}
.abs{position:absolute}
.layer{position:absolute;left:0;top:0;width:878px;height:476px}

/* brand */
.brand{left:22px;top:38px;display:flex;align-items:center;gap:12px}
.brand__dot{width:30px;height:30px;border-radius:50%;background:var(--teal-dark)}
.brand__name{font:700 38px/1 "Roboto",Arial,sans-serif;color:var(--teal-dark);letter-spacing:.3px}

.headline-band{left:0;top:106px;width:472px;height:70px;background:var(--teal-dark);padding:12px 0 0 23px;color:var(--white);font:500 21px/28px "Roboto",Arial,sans-serif}

.services{display:grid;grid-template-columns:228px 200px;left:26px;top:184px;row-gap:3.5px;font-size:13.6px;line-height:16.5px}
.check{position:relative;padding-left:16px}
.check::before{content:"";position:absolute;left:0;top:4px;width:9px;height:9px;border:1.2px solid var(--sage);border-radius:1px}
.check::after{content:"";position:absolute;left:3px;top:3.5px;width:7px;height:4px;border-left:1.6px solid var(--sage);border-bottom:1.6px solid var(--sage);transform:rotate(-45deg)}

/* coupons */
.coupon{background:var(--sage);color:var(--white);text-align:center}
.coupon::before{content:"";position:absolute;inset:4px;border:1.5px dashed var(--white)}
.coupon__tab{position:absolute;left:50%;transform:translateX(-50%);top:-8px;width:117px;height:22px;background:var(--white);border-radius:7px;font:400 10.5px/24px "Open Sans",sans-serif;letter-spacing:2.2px;color:var(--sage);z-index:1}
.coupon__big{font:500 29px/1 "Oswald",sans-serif;letter-spacing:.3px}
.coupon__mid{font:500 20px/24px "Oswald",sans-serif}
.coupon__small{font:400 10.3px/13.5px "Open Sans",sans-serif}
.coupon--front{top:284px;width:166px;height:114px;padding-top:30px}
.coupon--front .coupon__big{margin-bottom:7px}
.coupon--front.is-kit{padding-top:33px}
.coupon--front.is-kit .coupon__mid{margin-bottom:3px}
.coupon--front.is-grout{padding-top:22px}

.trust-line{left:23px;top:409px;font:400 12px/1 "Oswald",sans-serif;color:var(--teal);letter-spacing:-.1px}
.slogan{right:10px;top:404px;font:400 16px/1 "Courgette",cursive;color:var(--teal-dark)}

/* footer bar */
.cta-bar{left:0;top:430px;width:878px;height:46px;color:var(--white)}
.cta-bar__text{left:24px;top:13px;font:400 14.5px/1 "Roboto",Arial,sans-serif}
.cta-bar__contact{top:11px;display:flex;align-items:center;gap:7px;font:400 19px/1 "Roboto",Arial,sans-serif}
.cta-bar__contact.is-phone{left:452px}
.cta-bar__contact.is-web{left:604px}

/* back */
.back-brand{left:18px;top:52px;display:flex;align-items:center;gap:7px}
.back-brand__dot{width:12px;height:12px;background:var(--white);flex:none}
.back-brand__name{font:700 19px/20px "Roboto",Arial,sans-serif;color:var(--white)}
.back-headline{left:158px;top:25px;font:500 19.5px/24px "Roboto",Arial,sans-serif;color:var(--white)}
.coupon--back{left:30px;top:115px;width:179px;height:120px;padding-top:31px;box-shadow:2px 3px 5px rgba(0,0,0,.25)}
.coupon--back .coupon__big{font-size:30px;margin-bottom:6px}
.coupon--back .coupon__sub{font:400 15px/1 "Open Sans",sans-serif;margin-bottom:8px}
.coupon--back .coupon__small{font-size:7.8px;line-height:9.5px}
.vacuum-lineup{left:252px;top:98px;width:156px;height:148px;border-radius:8px;background:linear-gradient(90deg,#7c7f80 0%,#9e2a2e 28%,#1f3b73 52%,#1c1c1c 75%,#a52a2f 100%);opacity:.85}
.before-after{border-radius:50%;border:7px solid var(--sage-light);box-shadow:0 2px 6px rgba(0,0,0,.25)}
.before-after.is-large{left:436px;top:106px;width:160px;height:160px;background:radial-gradient(circle at 40% 45%,#b39e86,#8c7660)}
.before-after.is-small{left:504px;top:222px;width:106px;height:106px;background:radial-gradient(circle at 55% 55%,#cfc7ba,#9e9689)}
.repair-band{left:0;top:254px;width:282px;height:34px;background:var(--teal-dark);color:var(--white);font:500 19.5px/34px "Roboto",Arial,sans-serif;padding-left:27px}
.repair-list{left:26px;top:302px;font-size:13.6px;line-height:20px}
.repair-note{padding-left:16px}
.brand-grid{left:296px;top:270px;display:grid;grid-template-columns:repeat(4,48px);gap:6px 6px}
.brand-grid span{height:10px;border-radius:2px;background:#c9cccb}
.brand-grid span.is-accent{background:#d9a4a4}
.brand-grid span.is-blue{background:#a9b6cf}

.location{left:605px;top:32px;font:400 11.5px/16px "Roboto",Arial,sans-serif;color:var(--text-grey)}
.indicia{left:785px;top:24px;width:78px;height:78px;border:1.5px solid #222;font:700 9.5px/12px "Roboto",Arial,sans-serif;color:#111;text-align:center;padding-top:8px}
.address-box{left:636px;top:147px;width:226px;height:79px;border:1px solid #555;font:400 12.5px/13.5px "Roboto",Arial,sans-serif;color:#111}
.address-box__route{position:absolute;right:16px;top:10px;font-size:9.5px;letter-spacing:.3px}
.address-box__to{position:absolute;left:16px;top:38px}
.review{left:568px;top:365px;width:300px}
.review__stars{display:flex;gap:2px;margin-bottom:5px}
.review__text{font:400 10.5px/13.5px "Roboto",Arial,sans-serif;color:var(--text-grey)}
</style>
</head>
<body>

<!-- FRONT: cleaning services -->
<section class="card card--front">
  <svg class="layer" viewBox="0 0 878 476" role="img" aria-label="Photo of a smiling family lying on a freshly cleaned white carpet">
    <defs>
      <linearGradient id="familyTone" x1="0" y1="0" x2="1" y2="1">
        <stop offset="0" stop-color="#e9ecea"/>
        <stop offset=".55" stop-color="#d2c8bd"/>
        <stop offset="1" stop-color="#f1f1ee"/>
      </linearGradient>
    </defs>
    <path d="M512 0 C470 80 468 200 492 280 L878 280 L878 0 Z" fill="url(#familyTone)"/>
    <path d="M500 0 C458 80 456 200 480 280" fill="none" stroke="var(--sage)" stroke-width="9"/>
    <path d="M512 0 C470 80 468 200 492 280" fill="none" stroke="var(--sage-light)" stroke-width="5"/>
  </svg>

  <div class="abs brand"><span class="brand__dot"></span><span class="brand__name">HARBOR VACUUMS</span></div>

  <h1 class="abs headline-band">CARPETS &amp; FLOORING NEED CLEANING?<br>FURNITURE NEED CLEANING?</h1>

  <ul class="abs services" style="list-style:none">
    <li class="check">Commercial</li><li class="check">Carpet Cleaning</li>
    <li class="check">Residential</li><li class="check">Tile &amp; Grout Cleaning</li>
    <li class="check">General Cleaning</li><li class="check">VCT Strip &amp; Wax</li>
    <li class="check">Move In &amp; Move Out Cleanings</li><li class="check">Furniture Cleaning</li>
  </ul>

  <div class="abs coupon coupon--front" style="left:2px">
    <span class="coupon__tab">COUPON</span>
    <div class="coupon__big">ONLY $189</div>
    <div class="coupon__small">Whole House Carpet<br>Cleaning Up To 700 Sq Ft</div>
  </div>
  <div class="abs coupon coupon--front" style="left:178px">
    <span class="coupon__tab">COUPON</span>
    <div class="coupon__big">ONLY $199</div>
    <div class="coupon__small">Furniture Cleaning<br>(Sofa, Loveseat &amp; Chair)</div>
  </div>
  <div class="abs coupon coupon--front" style="left:354px">
    <span class="coupon__tab">COUPON</span>
    <div class="coupon__big">ONLY $119</div>
    <div class="coupon__small">Tile &amp; Grout Cleaning<br>Kitchen Floor Only<br>(Up To 120 Sq Ft)</div>
  </div>
  <div class="abs coupon coupon--front is-kit" style="left:531px">
    <span class="coupon__tab">COUPON</span>
    <div class="coupon__mid">FREE CLEANING KIT</div>
    <div class="coupon__small">(Value of $59)<br>for Your Carpet When<br>You Add Protector</div>
  </div>
  <div class="abs coupon coupon--front is-grout" style="left:709px">
    <span class="coupon__tab">COUPON</span>
    <div class="coupon__mid">FREE TILE &amp; GROUT<br>CLEANING KIT</div>
    <div class="coupon__small" style="margin-top:3px">(Value of $59)<br>When you Add Sealer</div>
  </div>

  <p class="abs trust-line">FRIENDLY, PROFESSIONAL, OTWAB TRAINED TECHNICIANS</p>
  <p class="abs slogan">Nobody Does It Better &amp; Gives You More</p>

  <footer class="abs cta-bar">
    <svg class="layer" style="height:46px" viewBox="0 0 878 46" aria-hidden="true">
      <defs><linearGradient id="barFront" x1="0" x2="1"><stop offset="0" stop-color="#5f8b81"/><stop offset="1" stop-color="var(--teal-dark)"/></linearGradient></defs>
      <rect width="878" height="46" fill="url(#barFront)"/>
      <polygon points="0,0 448,0 430,46 0,46" fill="var(--teal-dark)"/>
    </svg>
    <span class="abs cta-bar__text">Call us for a FREE Estimates on ALL Your Cleaning Needs!</span>
    <span class="abs cta-bar__contact is-phone">
      <svg width="18" height="18" viewBox="0 0 20 20" aria-hidden="true"><circle cx="10" cy="10" r="8.5" fill="none" stroke="#fff" stroke-width="1.4"/><path d="M7 5.5l1.6 2.2-.9 1.2c.6 1.3 1.5 2.2 2.8 2.8l1.2-.9 2.2 1.6-.8 1.6c-3.6-.2-7.2-3.8-7.4-7.4z" fill="#fff"/></svg>555-013-4827</span>
    <span class="abs cta-bar__contact is-web">
      <svg width="17" height="17" viewBox="0 0 20 20" aria-hidden="true"><g fill="none" stroke="#fff" stroke-width="1.3"><circle cx="10" cy="10" r="8.5"/><ellipse cx="10" cy="10" rx="3.8" ry="8.5"/><path d="M1.5 10h17M3 5.5h14M3 14.5h14"/></g></svg>www.HarborVacuums.com</span>
  </footer>
</section>

<!-- BACK: vacuum repair -->
<section class="card card--back">
  <svg class="layer" viewBox="0 0 878 476" aria-hidden="true">
    <defs>
      <linearGradient id="headerTone" x1="0" x2="1"><stop offset="0" stop-color="#9fb8b1"/><stop offset=".35" stop-color="#6b9188"/><stop offset="1" stop-color="#6f958b"/></linearGradient>
    </defs>
    <path d="M0 0 L458 0 C492 22 512 55 522 90 L0 90 Z" fill="url(#headerTone)"/>
    <path d="M0 90 L522 90 C532 140 536 200 536 254 L0 254 Z" fill="var(--grey-panel)"/>
    <path d="M462 0 C520 40 538 150 536 430" fill="none" stroke="var(--sage)" stroke-width="10"/>
    <path d="M478 0 C530 40 548 150 548 430" fill="none" stroke="var(--sage-light)" stroke-width="6"/>
  </svg>

  <div class="abs back-brand"><span class="back-brand__dot"></span><span class="back-brand__name">HARBOR<br>VACUUMS</span></div>
  <h2 class="abs back-headline">ARE YOU FRUSTRATED<br>WITH YOUR VACUUM CLEANER?!</h2>

  <div class="abs coupon coupon--back">
    <span class="coupon__tab">COUPON</span>
    <div class="coupon__big">ONLY $19.99</div>
    <div class="coupon__sub">Vacuum Tune Up</div>
    <div class="coupon__small">*Offer Expires in 30 days<br>**Limit One Vacuum Per Coupon</div>
  </div>

  <div class="abs vacuum-lineup" role="img" aria-label="Row of upright and canister vacuum cleaners in grey, red, blue and black"></div>
  <div class="abs before-after is-large" role="img" aria-label="Before and after close-up of carpet being cleaned"></div>
  <div class="abs before-after is-small" role="img" aria-label="Carpet cleaning wand passing over a carpet"></div>

  <h3 class="abs repair-band">Our Repair Center Offers:</h3>
  <ul class="abs repair-list" style="list-style:none">
    <li class="check">Free Estimates</li>
    <li class="check">Experienced &amp; Trained Technicians</li>
    <li class="check">Fast, reliable service</li>
    <li class="check">Courtesy(loaner vacuums)</li>
    <li class="check">Drive Up (Curbside Service)</li>
    <li class="repair-note">(Pull in, honk, call or blink your lights and we’ll carry the vacuum in for you)</li>
  </ul>

  <div class="abs brand-grid" aria-label="Vacuum brands serviced">
    <span></span><span class="is-blue"></span><span></span><span class="is-blue"></span>
    <span class="is-accent"></span><span class="is-blue"></span><span class="is-accent"></span><span class="is-blue"></span>
    <span class="is-accent"></span><span class="is-accent"></span><span class="is-accent"></span><span></span>
    <span class="is-accent"></span><span class="is-blue"></span><span></span><span></span>
    <span class="is-blue"></span><span></span><span></span><span class="is-accent"></span>
    <span class="is-accent"></span><span class="is-accent"></span><span class="is-accent"></span><span class="is-blue"></span>
    <span style="visibility:hidden"></span><span style="visibility:hidden"></span><span class="is-blue"></span>
  </div>

  <p class="abs location">Conveniently located at:<br>2841 Linden Ave<br>Millbrook, NY 12990<br>*Just off Route 9 Exit 4</p>

  <div class="abs indicia">PRSRT STD<br>ECRWSS<br>U.S. POSTAGE<br>PAID<br>KTRW RETAIL</div>

  <div class="abs address-box">
    <span class="address-box__route">*****************ECRWSS****</span>
    <span class="address-box__to">Local<br>Postal Customer</span>
  </div>

  <div class="abs review">
    <div class="review__stars" aria-label="5 stars">
      <svg width="90" height="17" viewBox="0 0 90 17" aria-hidden="true"><g fill="var(--star)">
        <polygon points="8.5,0 11,5.6 17,6.2 12.5,10.2 13.8,16.2 8.5,13.1 3.2,16.2 4.5,10.2 0,6.2 6,5.6"/>
        <polygon transform="translate(18 0)" points="8.5,0 11,5.6 17,6.2 12.5,10.2 13.8,16.2 8.5,13.1 3.2,16.2 4.5,10.2 0,6.2 6,5.6"/>
        <polygon transform="translate(36 0)" points="8.5,0 11,5.6 17,6.2 12.5,10.2 13.8,16.2 8.5,13.1 3.2,16.2 4.5,10.2 0,6.2 6,5.6"/>
        <polygon transform="translate(54 0)" points="8.5,0 11,5.6 17,6.2 12.5,10.2 13.8,16.2 8.5,13.1 3.2,16.2 4.5,10.2 0,6.2 6,5.6"/>
        <polygon transform="translate(72 0)" points="8.5,0 11,5.6 17,6.2 12.5,10.2 13.8,16.2 8.5,13.1 3.2,16.2 4.5,10.2 0,6.2 6,5.6"/>
      </g></svg>
    </div>
    <p class="review__text">"Ned and Walt have great customer skills. It's enjoyable to shop there. Very friendly atmosphere." - Miles R.</p>
  </div>

  <footer class="abs cta-bar">
    <svg class="layer" style="height:46px" viewBox="0 0 878 46" aria-hidden="true">
      <defs><linearGradient id="barBack" x1="0" x2="1"><stop offset="0" stop-color="#5f8b81"/><stop offset="1" stop-color="var(--teal-dark)"/></linearGradient></defs>
      <rect width="878" height="46" fill="url(#barBack)"/>
      <polygon points="0,0 448,0 430,46 0,46" fill="var(--teal-dark)"/>
    </svg>
    <span class="abs cta-bar__text">Call us for a FREE Estimates on ALL Your Cleaning Needs!</span>
    <span class="abs cta-bar__contact is-phone">
      <svg width="18" height="18" viewBox="0 0 20 20" aria-hidden="true"><circle cx="10" cy="10" r="8.5" fill="none" stroke="#fff" stroke-width="1.4"/><path d="M7 5.5l1.6 2.2-.9 1.2c.6 1.3 1.5 2.2 2.8 2.8l1.2-.9 2.2 1.6-.8 1.6c-3.6-.2-7.2-3.8-7.4-7.4z" fill="#fff"/></svg>555-013-4827</span>
    <span class="abs cta-bar__contact is-web">
      <svg width="17" height="17" viewBox="0 0 20 20" aria-hidden="true"><g fill="none" stroke="#fff" stroke-width="1.3"><circle cx="10" cy="10" r="8.5"/><ellipse cx="10" cy="10" rx="3.8" ry="8.5"/><path d="M1.5 10h17M3 5.5h14M3 14.5h14"/></g></svg>www.HarborVacuums.com</span>
  </footer>
</section>

</body>
</html>
```